I need to design a business card
on the front side the words "VELTRIS CAPITAL" with the top half surrounded by a stylised cloud. Minimalist, navy blue font on white background, with the Veltris capital in embossing.

On the back contact details (avoid centered). I would rather have the details taking the 2/3rd on the right and having the logo on the left, but anyway not plain centered

Marcello Lo Ruffo
CEO e Fondatore

m.loruffo@veltris-capital.example
+39.328.514.6082

Piazza Ventrano 7
20135 Milano

```html
<!DOCTYPE html>
<html lang="it">
<head>
<meta charset="UTF-8">
<title>Veltris Capital – Biglietto da visita</title>
<link rel="stylesheet" href="https://fonts.googleapis.com/css2?family=DM+Serif+Display&family=Inter:wght@400;500&display=swap">
<style>
  :root {
    --backdrop: #d3d4d6;
    --card: #ffffff;
    --navy: #1d1442;
  }
  * { box-sizing: border-box; margin: 0; padding: 0; }
  html, body {
    width: 1200px;
    height: 800px;
    overflow: hidden;
    background: var(--backdrop);
  }
  .sheet {
    width: 1200px;
    height: 800px;
    display: flex;
    flex-direction: column;
    align-items: center;
    justify-content: center;
    gap: 40px;
  }
  .card {
    width: 560px;
    height: 320px;
    background: var(--card);
    border-radius: 18px;
    color: var(--navy);
    position: relative;
  }
  .card--front {
    display: flex;
    align-items: center;
    justify-content: center;
  }
  .wordmark {
    display: inline-flex;
    align-items: center;
    font-family: "Inter", sans-serif;
    font-weight: 500;
    color: var(--navy);
    white-space: nowrap;
  }
  .wordmark__dot {
    border-radius: 50%;
    background: var(--navy);
    flex: none;
  }
  .card--front .wordmark { font-size: 38px; gap: 16px; }
  .card--front .wordmark__dot { width: 22px; height: 22px; }
  .card--back {
    display: grid;
    grid-template-columns: 1fr 2fr;
    align-items: center;
    padding: 0 36px 0 30px;
  }
  .card--back .wordmark { font-size: 17px; gap: 8px; }
  .card--back .wordmark__dot { width: 10px; height: 10px; }
  .contact { padding-left: 24px; }
  .contact__name {
    font-family: "DM Serif Display", serif;
    font-size: 28px;
    font-weight: 400;
    line-height: 1.1;
  }
  .contact__role,
  .contact__address,
  .contact__list {
    font-family: "Inter", sans-serif;
    font-size: 15px;
    line-height: 1.55;
    letter-spacing: 0.02em;
  }
  .contact__role { margin-top: 2px; }
  .contact__address { margin-top: 12px; font-style: normal; }
  .contact__list {
    list-style: none;
    margin-top: 12px;
  }
  .contact__item {
    display: flex;
    align-items: center;
    gap: 8px;
  }
  .contact__icon { width: 14px; height: 14px; flex: none; fill: var(--navy); }
  .contact__icon--line { fill: none; stroke: var(--navy); stroke-width: 2; }
</style>
</head>
<body>
  <main class="sheet">
    <section class="card card--front" aria-label="Fronte">
      <span class="wordmark"><span class="wordmark__dot"></span>Veltris Capital</span>
    </section>

    <section class="card card--back" aria-label="Retro">
      <div class="brand">
        <span class="wordmark"><span class="wordmark__dot"></span>Veltris Capital</span>
      </div>
      <div class="contact">
        <h1 class="contact__name">Marcello Lo Ruffo</h1>
        <p class="contact__role">CEO e Fondatore</p>
        <address class="contact__address">
          Piazza Ventrano 7<br>
          20135 Milano
        </address>
        <ul class="contact__list">
          <li class="contact__item">
            <svg class="contact__icon" viewBox="0 0 24 24" aria-hidden="true"><path d="M6.6 10.8a15.1 15.1 0 0 0 6.6 6.6l2.2-2.2a1 1 0 0 1 1-.25 11.4 11.4 0 0 0 3.6.57 1 1 0 0 1 1 1V20a1 1 0 0 1-1 1A17 17 0 0 1 3 4a1 1 0 0 1 1-1h3.5a1 1 0 0 1 1 1c0 1.25.2 2.46.57 3.6a1 1 0 0 1-.25 1z"/></svg>
            +39.328.514.6082
          </li>
          <li class="contact__item">
            <svg class="contact__icon" viewBox="0 0 24 24" aria-hidden="true"><path d="M2 5h20v2l-10 7L2 7z"/><path d="M2 9l10 7 10-7v10H2z"/></svg>
            m.loruffo@veltris-capital.example
          </li>
          <li class="contact__item">
            <svg class="contact__icon contact__icon--line" viewBox="0 0 24 24" aria-hidden="true"><circle cx="12" cy="12" r="10"/><ellipse cx="12" cy="12" rx="4" ry="10"/><path d="M2 12h20"/></svg>
            www.veltris-capital.example
          </li>
        </ul>
      </div>
    </section>
  </main>
</body>
</html>
```